Zebra Romp - mobile play centre poster designs

Who are we - we are a mobile playground business that specialises in providing entertainment to children in a safe, clean environment either at home or in a function centre. Brief - create 4 different signs to be displayed on our playgrounds. Please find attached 3 photos from our competitors to use as a guide. Corflute sign - size A1 Toddler zone - size A1 Playground rules - size A4 No climbing - size 20cmx8cm sending through photos and documents now.
Colors
Designer to choose colors to be used in the design.
Requirements
Must have
- Colour, be very specific with the rules, pictures

```html
<!DOCTYPE html>
<html lang="en">
<head>
<meta charset="utf-8">
<title>Zebra Romp – Play Centre Signage</title>
<link href="https://fonts.googleapis.com/css2?family=Figtree:wght@400;500;700;800;900&family=Rammetto+One&display=swap" rel="stylesheet">
<style>
  :root{
    --board:#1f1f21;
    --white:#ffffff;
    --yellow:#ffe000;
    --maroon:#7a2540;
    --rules-a:#ff5a84;
    --rules-b:#ff8a6e;
    --toddler-a:#5b3cff;
    --toddler-b:#a45cff;
    --toddler-ink:#5a3fc8;
    --climb-a:#fba65c;
    --climb-b:#fad06f;
    --stop-red:#e8402f;
    --brown:#6a3a12;
    --banner-a:#6682f5;
    --banner-b:#58d5fb;
    --caption:#ffffff;
  }
  *{box-sizing:border-box;margin:0;padding:0}
  html,body{width:1200px;height:1126px;overflow:hidden;background:var(--board)}
  body{position:relative;font-family:"Figtree",sans-serif;color:var(--white)}
  .sign{position:absolute;overflow:hidden}
  .sign__bg{position:absolute;inset:0}
  .poster{top:39px;width:341px;height:484px}
  .poster--rules{left:50px}
  .poster--rules .sign__bg{background:linear-gradient(160deg,var(--rules-a) 0%,var(--rules-a) 55%,var(--rules-b) 100%)}
  .poster--toddler{left:429px}
  .poster--toddler .sign__bg{background:linear-gradient(165deg,var(--toddler-a) 0%,var(--toddler-a) 60%,var(--toddler-b) 100%)}
  .poster--climb{left:808px}
  .poster--climb .sign__bg{background:linear-gradient(165deg,var(--climb-a) 0%,var(--climb-a) 55%,var(--climb-b) 100%)}
  .caption{position:absolute;font-size:18px;font-weight:400;color:var(--caption)}
  .brand{position:absolute;font-weight:500;font-size:36px;color:var(--white);letter-spacing:-.3px;line-height:1;white-space:nowrap}
  .poster .brand{left:32px;top:36px}
  .band{position:absolute;left:0;background:var(--yellow);border-radius:0 22px 22px 0;height:44px;display:flex;align-items:center;font-family:"Rammetto One",sans-serif;white-space:nowrap}
  .hl{color:var(--yellow)}

  /* rules poster */
  .rules__intro{position:absolute;left:32px;top:111px;width:290px;font-size:12.6px;font-weight:700;line-height:17px}
  .rules__band{top:154px;width:311px;padding-left:32px;color:var(--maroon);font-size:21px}
  .rules__band small{font-size:13px;margin-left:8px}
  .rule{position:absolute;display:flex;align-items:flex-start;gap:9px}
  .rule__icon{width:47px;height:47px;flex:none}
  .rule__text{padding-top:0}
  .rule__no{display:block;font-size:18px;font-weight:900;color:var(--yellow);line-height:21px}
  .rule__what{display:block;font-size:10.8px;font-weight:700;line-height:13px}
  .rule__note{display:block;font-size:7.5px;font-weight:700;line-height:10px}

  /* toddler poster */
  .toddler__band{top:102px;width:243px;padding-left:31px;color:var(--toddler-ink);font-size:21px}
  .toddler__age{position:absolute;left:33px;top:154px;font-size:19px;font-weight:900;color:var(--yellow)}
  .toddler__line{position:absolute;left:33px;font-size:12.6px;font-weight:700}
  .toddler__notice{position:absolute;left:97px;top:230px;width:212px;height:224px;border:3px solid var(--yellow);border-radius:14px;padding:13px 16px 0 18px;font-size:11.8px;font-weight:700;line-height:17.1px;text-align:justify}

  /* climb poster */
  .climb__sign{position:absolute;left:87px;top:119px;width:166px;height:166px}
  .climb__no{position:absolute;left:0;right:0;top:290px;text-align:center;font-weight:900;font-size:74px;color:var(--stop-red);line-height:1;letter-spacing:-2px}
  .climb__word{position:absolute;left:0;right:0;top:365px;text-align:center;font-weight:700;font-size:46px;color:var(--brown);line-height:1}

  /* banner */
  .banner{left:50px;top:604px;width:1103px;height:441px}
  .banner .sign__bg{background:linear-gradient(90deg,var(--banner-a) 0%,var(--banner-b) 14%,var(--banner-b) 72%,var(--banner-a) 100%)}
  .banner .brand{left:793px;top:28px}
</style>
</head>
<body>

<!-- Playground rules -->
<section class="sign poster poster--rules">
  <div class="sign__bg" role="img" aria-label="Soft pink and coral abstract background pattern"></div>
  <div class="brand">Zebra Romp</div>
  <p class="rules__intro"><span class="hl">Parents/Guardians</span> must supervise children using this play equipment at all times.</p>
  <div class="band rules__band">PLAY GROUND<small>Rules</small></div>

  <div class="rule" style="left:31px;top:221px">
    <svg class="rule__icon" viewBox="0 0 48 48" role="img" aria-label="Photo of shoes"><circle cx="24" cy="24" r="21" fill="#f0a060"/><circle cx="24" cy="24" r="21" fill="none" stroke="var(--maroon)" stroke-width="4"/><line x1="10" y1="10" x2="38" y2="38" stroke="var(--maroon)" stroke-width="4"/></svg>
    <div class="rule__text"><span class="rule__no">No!</span><span class="rule__what">Shoes</span><span class="rule__note">( Socks must be<br>worn )</span></div>
  </div>
  <div class="rule" style="left:181px;top:221px">
    <svg class="rule__icon" viewBox="0 0 48 48" role="img" aria-label="Photo of climbing on nets"><circle cx="24" cy="24" r="21" fill="#8a8a62"/><circle cx="24" cy="24" r="21" fill="none" stroke="var(--maroon)" stroke-width="4"/><line x1="10" y1="10" x2="38" y2="38" stroke="var(--maroon)" stroke-width="4"/></svg>
    <div class="rule__text"><span class="rule__no">No!</span><span class="rule__what">Climbing the<br>Nets</span></div>
  </div>
  <div class="rule" style="left:31px;top:283px">
    <svg class="rule__icon" viewBox="0 0 48 48" role="img" aria-label="Photo of food and drink"><circle cx="24" cy="24" r="21" fill="#c6803e"/><circle cx="24" cy="24" r="21" fill="none" stroke="var(--maroon)" stroke-width="4"/><line x1="10" y1="10" x2="38" y2="38" stroke="var(--maroon)" stroke-width="4"/></svg>
    <div class="rule__text"><span class="rule__no">No!</span><span class="rule__what">Food or Drink</span></div>
  </div>
  <div class="rule" style="left:181px;top:283px">
    <svg class="rule__icon" viewBox="0 0 48 48" role="img" aria-label="Photo of bottles and glasses"><circle cx="24" cy="24" r="21" fill="#d9cfc4"/><circle cx="24" cy="24" r="21" fill="none" stroke="var(--maroon)" stroke-width="4"/><line x1="10" y1="10" x2="38" y2="38" stroke="var(--maroon)" stroke-width="4"/></svg>
    <div class="rule__text"><span class="rule__no">No!</span><span class="rule__what">Bottle or Glass</span></div>
  </div>
  <div class="rule" style="left:31px;top:346px">
    <svg class="rule__icon" viewBox="0 0 48 48" role="img" aria-label="Photo of chewing gum packs"><circle cx="24" cy="24" r="21" fill="#7fa6c9"/><circle cx="24" cy="24" r="21" fill="none" stroke="var(--maroon)" stroke-width="4"/><line x1="10" y1="10" x2="38" y2="38" stroke="var(--maroon)" stroke-width="4"/></svg>
    <div class="rule__text"><span class="rule__no">No!</span><span class="rule__what">Chewing Gum</span></div>
  </div>
  <div class="rule" style="left:181px;top:346px">
    <svg class="rule__icon" viewBox="0 0 48 48" role="img" aria-label="Photo of sharp tools"><circle cx="24" cy="24" r="21" fill="#d8d8d8"/><circle cx="24" cy="24" r="21" fill="none" stroke="var(--maroon)" stroke-width="4"/><line x1="10" y1="10" x2="38" y2="38" stroke="var(--maroon)" stroke-width="4"/></svg>
    <div class="rule__text"><span class="rule__no">No!</span><span class="rule__what">Sharp Objects</span></div>
  </div>
  <div class="rule" style="left:31px;top:408px">
    <svg class="rule__icon" viewBox="0 0 48 48" role="img" aria-label="Photo of face painting"><circle cx="24" cy="24" r="21" fill="#e6cfc0"/><circle cx="24" cy="24" r="21" fill="none" stroke="var(--maroon)" stroke-width="4"/><line x1="10" y1="10" x2="38" y2="38" stroke="var(--maroon)" stroke-width="4"/></svg>
    <div class="rule__text"><span class="rule__no">No!</span><span class="rule__what">Face Painting</span></div>
  </div>
</section>
<div class="caption" style="left:50px;top:540px">A1 Size - Playground rules</div>

<!-- Toddler zone -->
<section class="sign poster poster--toddler">
  <div class="sign__bg" role="img" aria-label="Soft violet and pink abstract background pattern"></div>
  <div class="brand">Zebra Romp</div>
  <div class="band toddler__band">Toddler Zone</div>
  <div class="toddler__age">0-3 year olds ONLY</div>
  <div class="toddler__line" style="top:178px">Supervision required at all times.</div>
  <div class="toddler__line" style="top:196px">• Parents please <span class="hl">wear socks</span> too</div>
  <div class="toddler__notice">If using the toddler soft play equipment, please ensure that this area is used by <span class="hl">children 0-3 ONLY</span>. The equipment and ball pit is only designed for small children and bigger kids might injure themselves, the smaller children or <span class="hl">cause extensive damage</span> to the equipment, of which there will be a <span class="hl">charge back</span> to the client.</div>
</section>
<div class="caption" style="left:429px;top:540px">A1 Size - Toddler Zone</div>

<!-- No climbing -->
<section class="sign poster poster--climb">
  <div class="sign__bg" role="img" aria-label="Soft orange and yellow abstract background pattern"></div>
  <div class="brand">Zebra Romp</div>
  <svg class="climb__sign" viewBox="0 0 166 166">
    <circle cx="83" cy="83" r="70" fill="#7e8f5c" role="img" aria-label="Photo of a person climbing a rope net"/>
    <circle cx="83" cy="83" r="76" fill="none" stroke="var(--stop-red)" stroke-width="13"/>
    <line x1="130" y1="36" x2="36" y2="130" stroke="var(--stop-red)" stroke-width="9"/>
  </svg>
  <div class="climb__no">No!</div>
  <div class="climb__word">Climbing</div>
</section>
<div class="caption" style="left:808px;top:540px">A4 Size - No Climbing</div>

<!-- Corflute banner -->
<section class="sign banner">
  <div class="sign__bg" role="img" aria-label="Soft sky blue and periwinkle abstract background pattern"></div>
  <div class="brand">Zebra Romp</div>
</section>
<div class="caption" style="left:50px;top:1061px">20cm x 8cm</div>

</body>
</html>
```